Lantern Motion for Neighbors Business Cards

I need business cards for staff in a new startup. Our company name is Movrela - we train Tai Chi teachers. But our biggest project is called Lantern Motion for Neighbors - a federal project to put together free Tai Chi classes for Vets all across America. It's a young company, with a spirit of excitement, passion, a desire to do good for others (our Vets) and a modern style and sensibility. In other words, not old-fashioned Asian martial arts theme, but something new.

Industry/Entity Type

Health And Wellness

Contact Information for Business Card

The topic is ancient healing, but the company is the Pembrooks - so I'd like a card design that captures that.

Font styles to use
Sans Serif

Colors

Designer to choose colors to be used in the design.

Requirements
Nice to have
• I've got two logos - one for the company and one for the project. I want to see if we can incorporate them both without it becoming too busy.
Should not have
• Overly old-fashioned yin-yang themes.

```html
<!DOCTYPE html>
<html lang="en">
<head>
<meta charset="utf-8">
<title>Lantern Motion for Neighbors — Business Cards</title>
<link rel="stylesheet" href="https://fonts.googleapis.com/css2?family=Montserrat:wght@400;500;600&display=swap">
<style>
  :root {
    --backdrop: #2b2b2d;
    --card: #050506;
    --navy: #2f2b80;
    --red: #e3202b;
    --text-navy: #3a3594;
    --font: "Montserrat", sans-serif;
  }
  * { margin: 0; padding: 0; box-sizing: border-box; }
  html, body { width: 1200px; height: 900px; overflow: hidden; }
  body {
    background: var(--backdrop);
    font-family: var(--font);
    position: relative;
  }
  .card {
    position: absolute;
    left: 250px;
    width: 700px;
    height: 400px;
    background: var(--card);
    overflow: hidden;
    box-shadow: 0 10px 30px rgba(0,0,0,.45);
  }
  .card--front { top: 40px; }
  .card--back { top: 460px; }
  .card__waves { position: absolute; inset: 0; width: 100%; height: 100%; }

  .brand { position: absolute; display: flex; align-items: center; gap: 14px; }
  .brand__dot { border-radius: 50%; flex: none; }
  .brand__name {
    color: var(--text-navy);
    font-weight: 500;
    text-transform: uppercase;
    line-height: 1.15;
    letter-spacing: .04em;
  }
  .brand--project { left: 60px; top: 150px; }
  .brand--project .brand__dot { width: 74px; height: 74px; border: 3px solid var(--navy); }
  .brand--project .brand__name { font-size: 25px; width: 260px; }

  .brand--company { right: 60px; top: 50px; }
  .brand--company .brand__dot { width: 64px; height: 64px; background: var(--red); }
  .brand--company .brand__name { color: var(--red); font-size: 26px; }

  .brand--back { left: 36px; top: 40px; }
  .brand--back .brand__dot { width: 56px; height: 56px; border: 3px solid var(--navy); }
  .brand--back .brand__name { font-size: 19px; width: 220px; }

  .person {
    position: absolute;
    right: 50px;
    top: 110px;
    width: 260px;
    text-align: right;
    padding-bottom: 8px;
    border-bottom: 1px solid var(--navy);
  }
  .person__name { color: var(--text-navy); font-size: 24px; font-weight: 500; text-transform: uppercase; }
  .person__role { color: var(--red); font-size: 15px; font-weight: 500; }

  .contacts {
    position: absolute;
    left: 60px;
    top: 268px;
    width: 320px;
    border-top: 1px solid var(--navy);
    padding-top: 10px;
    list-style: none;
  }
  .contacts li {
    display: flex; align-items: center; gap: 12px;
    color: var(--text-navy); font-size: 15px; line-height: 25px;
  }
  .contacts svg { width: 14px; height: 14px; flex: none; }
</style>
</head>
<body>

<section class="card card--front">
  <svg class="card__waves" viewBox="0 0 700 400" aria-hidden="true">
    <path fill="var(--navy)" d="M0,330 H300 C345,330 360,300 405,292 L700,238 V252 L420,306 C385,312 372,348 345,400 H0 Z"/>
    <path fill="var(--red)" d="M345,400 C372,348 385,312 420,306 L700,252 V268 L436,322 C410,328 400,360 385,400 Z"/>
    <path fill="var(--navy)" d="M436,330 L700,276 V284 L440,338 Z"/>
  </svg>
  <div class="brand brand--project">
    <span class="brand__dot"></span>
    <span class="brand__name">Lantern Motion for Neighbors</span>
  </div>
  <div class="brand brand--company">
    <span class="brand__dot"></span>
    <span class="brand__name">Movrela</span>
  </div>
</section>

<section class="card card--back">
  <svg class="card__waves" viewBox="0 0 700 400" aria-hidden="true">
    <path fill="var(--navy)" d="M700,150 V230 L520,262 C545,215 560,198 600,185 Z"/>
    <path fill="var(--red)" d="M60,395 L560,260 L700,228 V246 L470,300 L100,400 H60 Z"/>
    <path fill="var(--navy)" d="M120,400 L700,254 V266 L170,400 Z"/>
  </svg>
  <div class="brand brand--back">
    <span class="brand__dot"></span>
    <span class="brand__name">Lantern Motion for Neighbors</span>
  </div>
  <div class="person">
    <p class="person__name">Dana Whitcomb</p>
    <p class="person__role">Founder &amp; CEO</p>
  </div>
  <ul class="contacts">
    <li>
      <svg viewBox="0 0 24 24" fill="none" stroke="var(--red)" stroke-width="2"><path d="M5 3h4l2 5-2.5 1.5a11 11 0 0 0 6 6L16 13l5 2v4a2 2 0 0 1-2 2A16 16 0 0 1 3 5a2 2 0 0 1 2-2z"/></svg>
      <span>+00 000 481 2256</span>
    </li>
    <li>
      <svg viewBox="0 0 24 24" fill="none" stroke="var(--red)" stroke-width="2"><rect x="3" y="5" width="18" height="14"/><path d="M3 6l9 7 9-7"/></svg>
      <span>hello@movrela.co</span>
    </li>
    <li>
      <svg viewBox="0 0 24 24" fill="none" stroke="var(--red)" stroke-width="2"><circle cx="12" cy="12" r="9"/><path d="M3 12h18M12 3c3 3 3 15 0 18M12 3c-3 3-3 15 0 18"/></svg>
      <span>www.movrela.co</span>
    </li>
  </ul>
</section>

</body>
</html>
```